Exciting new branding of Recruitment Company based on it's new website

We have an exciting new website we are about to launch and would like to have letterhead, business cards, email signature options, email banner, linkedin and facebook cover images all refreshed to match the website. I have attached the existing logo. The website is at http://brightcrewstaff.hostpadsites.com/ and we are particularly interested in the grey with orange writing at the base of the first page where it says Register Now

Target Market(s)

Recruitment

Contact Information for Business Card

Dana Thorpe
Account Executive
T: 1300 582 318
M: 0412 736 085
E: dana@brightcrewstaff.com.au
W: brightcrewstaff.com.au
A: Suite 3, 42 Wattlebank Lane, Deakin ACT 2600
ABN: 52 184 637 905

Font styles to use
Serif
Sans Serif

Requirements
Must have
• The grey colour from the website

```html
<!DOCTYPE html>
<html lang="en">
<head>
<meta charset="utf-8">
<title>Bright Crew Stationery</title>
<link href="https://fonts.googleapis.com/css2?family=Lato:wght@400;700;900&display=swap" rel="stylesheet">
<style>
  :root {
    --orange: #f7941d;
    --grey: #6d6e70;
    --ink: #4a4a4a;
    --paper: #ffffff;
    --backdrop: #e6e2e1;
    --card-black: #111111;
    --rule: #3a3a3a;
  }
  * { box-sizing: border-box; margin: 0; padding: 0; }
  html, body { width: 883px; height: 1200px; overflow: hidden; }
  body {
    background: var(--backdrop);
    font-family: "Lato", Arial, sans-serif;
    color: var(--ink);
    position: relative;
  }

  /* Letterhead */
  .letterhead {
    position: absolute; left: 251px; top: 28px;
    width: 381px; height: 539px;
    background: var(--paper);
    box-shadow: 0 2px 8px rgba(0,0,0,.12);
    overflow: hidden;
  }
  .letterhead .brand {
    position: absolute; left: 34px; top: 34px;
    display: flex; align-items: center; gap: 8px;
  }
  .brand-dot {
    width: 30px; height: 30px; border-radius: 50%;
    border: 3px solid var(--orange);
  }
  .brand-name {
    font-weight: 900; color: var(--orange);
    font-size: 17px; line-height: 1; letter-spacing: -.2px;
  }
  .letterhead .sender {
    position: absolute; right: 30px; top: 36px;
    text-align: right; font-size: 6.3px; line-height: 1.55;
  }
  .sender .abn-label { color: var(--orange); }
  .letterhead .body {
    position: absolute; left: 34px; top: 104px; right: 34px;
    font-size: 7.2px; line-height: 1.55;
  }
  .body p { margin-bottom: 9px; }
  .body .signoff { margin-top: 4px; margin-bottom: 6px; }
  .signature {
    width: 30px; height: 14px; border-radius: 3px;
    background: linear-gradient(90deg, #fbd3a3, #f7b567);
  }
  .edge-band {
    position: absolute; left: 0; bottom: 0; width: 100%; height: 14px;
  }

  /* Business cards */
  .card {
    position: absolute; top: 645px;
    width: 394px; height: 225px;
    box-shadow: 0 3px 10px rgba(0,0,0,.2);
    overflow: hidden;
  }
  .card-back { left: 30px; background: var(--card-black); }
  .card-back .pattern {
    position: absolute; inset: 0;
    background: linear-gradient(135deg, #161616, #0c0c0c);
  }
  .card-back .brand-mark {
    position: absolute; left: 218px; top: 126px;
    display: flex; align-items: center; gap: 7px;
  }
  .card-back .brand-name { font-size: 16px; }

  .card-front { left: 459px; background: var(--paper); }
  .card-front .person {
    position: absolute; left: 20px; top: 20px;
  }
  .person-name {
    font-weight: 900; color: var(--orange); font-size: 17px; line-height: 1.1;
  }
  .person-role { font-size: 9.5px; margin-top: 2px; }
  .card-front .divider {
    position: absolute; left: 20px; right: 20px; top: 62px;
    height: 1px; background: var(--rule);
  }
  .contacts {
    position: absolute; left: 20px; top: 72px;
    list-style: none; font-size: 9.5px; line-height: 1;
  }
  .contacts li { display: flex; align-items: center; gap: 7px; margin-bottom: 5px; }
  .contacts svg { width: 9px; height: 9px; flex: none; }
  .card-front .brand {
    position: absolute; right: 22px; top: 78px;
    display: flex; align-items: center; gap: 8px;
  }
  .card-front .brand-dot { width: 34px; height: 34px; }
  .card-front .brand-name { font-size: 19px; }
  .card-front .divider-low {
    position: absolute; left: 190px; right: 20px; top: 142px;
    height: 1px; background: var(--rule);
  }
  .card-front .address {
    position: absolute; right: 22px; top: 152px;
    text-align: right; font-size: 10px; line-height: 1.45;
  }
  .card-front .edge-band { height: 22px; }
  .card-front .abn {
    position: absolute; right: 22px; bottom: 5px;
    color: #fff; font-size: 9.5px;
  }
</style>
</head>
<body>

<section class="letterhead">
  <div class="brand">
    <span class="brand-dot"></span>
    <span class="brand-name">bright crew</span>
  </div>
  <address class="sender">
    Suite 3, 42 Wattlebank Lane,<br>
    Deakin ACT 2600<br>
    1300 582 318<br>
    0412 736 085<br>
    dana@brightcrewstaff.com.au<br>
    www.brightcrewstaff.com.au<br>
    <span class="abn-label">ABN:</span> 52 184 637 905
  </address>
  <div class="body">
    <p>Dear Sir/Mam,</p>
    <p>Contrary to popular belief, Lorem Ipsum is not simply random text. It has roots in a piece of classical Latin literature from 45 BC, making it over 2000 years old. Ronald Halvorsen, a Latin professor at Ashgrove College in Virginia, looked up one of the more obscure Latin words, consectetur.</p>
    <p>Lorem Ipsum comes from sections 1.10.32 and 1.10.33 of "de Finibus Bonorum et Malorum" (The Extremes of Good and Evil) by Aurelian Tesk, written in 45 BC. This book is a treatise on the theory of ethics, very popular during the Renaissance. The first line of Lorem Ipsum.</p>
    <p>The standard chunk of Lorem Ipsum used since the 1500s is reproduced below for those interested. Sections 1.10.32 and 1.10.33 from "de Finibus Bonorum et Malorum" by Aurelian Tesk are also reproduced in their exact original.</p>
    <p>The standard chunk of Lorem Ipsum used since the 1500s is reproduced below for those interested.</p>
    <p class="signoff">Best Regards</p>
    <div class="signature" role="img" aria-label="Handwritten signature of Dana"></div>
  </div>
  <svg class="edge-band" viewBox="0 0 381 14" preserveAspectRatio="none" aria-hidden="true">
    <rect x="0" y="10" width="180" height="4" fill="var(--grey)"/>
    <polygon points="172,14 186,0 381,0 381,14" fill="var(--orange)"/>
  </svg>
</section>

<section class="card card-back">
  <div class="pattern" role="img" aria-label="Repeating tone-on-tone brand pattern on black"></div>
  <div class="brand-mark">
    <span class="brand-name">bright crew</span>
  </div>
</section>

<section class="card card-front">
  <div class="person">
    <div class="person-name">Dana Thorpe</div>
    <div class="person-role">Account Executive</div>
  </div>
  <div class="divider"></div>
  <ul class="contacts">
    <li>
      <svg viewBox="0 0 10 10" aria-hidden="true"><path d="M2 1h2l1 2.5-1.3 1a5 5 0 0 0 2.8 2.8l1-1.3L10 7v2a1 1 0 0 1-1 1A8 8 0 0 1 1 2a1 1 0 0 1 1-1z" fill="var(--orange)"/></svg>
      1300 582 318
    </li>
    <li>
      <svg viewBox="0 0 10 10" aria-hidden="true"><rect x="2.5" y="0.5" width="5" height="9" rx="1" fill="none" stroke="var(--orange)" stroke-width="1.2"/><circle cx="5" cy="8" r=".6" fill="var(--orange)"/></svg>
      0412 736 085
    </li>
    <li>
      <svg viewBox="0 0 10 10" aria-hidden="true"><rect x=".5" y="2" width="9" height="6.5" fill="var(--orange)"/><path d="M.8 2.3 5 5.8l4.2-3.5" fill="none" stroke="#fff" stroke-width=".9"/></svg>
      dana@brightcrewstaff.com.au
    </li>
    <li>
      <svg viewBox="0 0 10 10" aria-hidden="true"><circle cx="5" cy="5" r="4.3" fill="none" stroke="var(--orange)" stroke-width="1.1"/><path d="M.7 5h8.6M5 .7c-2.4 2.6-2.4 6 0 8.6M5 .7c2.4 2.6 2.4 6 0 8.6" fill="none" stroke="var(--orange)" stroke-width=".8"/></svg>
      www.brightcrewstaff.com.au
    </li>
  </ul>
  <div class="brand">
    <span class="brand-dot"></span>
    <span class="brand-name">bright crew</span>
  </div>
  <div class="divider-low"></div>
  <address class="address">
    Suite 3, 42 Wattlebank Lane,<br>
    Deakin ACT 2600
  </address>
  <svg class="edge-band" viewBox="0 0 394 22" preserveAspectRatio="none" aria-hidden="true">
    <rect x="0" y="17" width="200" height="5" fill="var(--grey)"/>
    <polygon points="190,22 210,6 394,6 394,22" fill="var(--orange)"/>
  </svg>
  <div class="abn">ABN: 52 184 637 905</div>
</section>

</body>
</html>
```